Business Card and Letterhead for Copperfield Reed - (Have Logo)

Update 4: Removed company reg no from business card details as it looked a bit out of place. Updated services list.
UPDATE 3
Sorry, I got the address a little bit wrong, have updated it below. Sorry for any inconvenience caused.
UPDATE 2
Finally I have the details for the business cards and letterhead. Submissions already made do not have to be updated unless shortlisted, if all new submissions could include the details for me, Simon, that would be very much appreciated and help with the final shortlist selection. I intend to share a shortlist of the three best entries with past and existing customers for their feedback and opinions. Thank you all again for your time.
Here are the details.
Simon Latchford
Web Developer
T: 01632 418 720
E: simon@copperfieldreed.example
www.copperfieldreed.example
Professional Photography
Web Solutions & E-Commerce
Audio & HD Video Production
Marketing & Promotions
Identity and Branding
Copperfield Reed Ltd
Suite 20938, 3rd Floor
212-224 Marlowe Row
London, EC2R 8KT
Company Reg. No: 09264183
The order and the layout of the information are of course down to the design, but the company registration number should be smaller and less prominent. The formatting of the telephone and email address using a T: and an E: I am not sure about and again if it is Tel: or Email: or Icons is up to the design.
The Company No. on the letterhead should read (somewhere in small text along the bottom):
Copperfield Reed is a Ltd Company registered in England & Wales, Registration No. 09264183.
The second business card details are
Martin Oakley
Photographer
T: 01632 418 720
E: martin@copperfieldreed.example
Everything else the same of course.
Thank you again for all the submissions so far.
END OF UPDATE 2
-
UPDATE 1: Please do not alter the logo nor the logo colours. (This was a previous pixel bazaar project and I am extremely happy with it. The icon can stand alone of course, but I have had to eliminate all entries that have made it black and white, or reversed the icon.) I would like to thank everyone that has participated so far and am very grateful for all your thought and time.
End of Update 1
-
Original Brief:
I have attached the logo vector file.
Following a superb logo from a previous Pixel Bazaar project I am now looking for a business card design and (although less important) a letterhead as well.
I must admit I tried to do it myself but could only come up with the usual amateur stuff that in comparison to the quality of the logo looked awful.
About Us
Copperfield Reed Ltd will be a new company due to start in January. It is really just me (a web developer) and my friend (a photographer). We will be aiming at the usual small to medium sized businesses in the local area, selling various digital services including photographic services to the public, web hosting and development, commercial photography, modelling services (not us!), full video and film production and possibly a bit of marketing as well. (Really it is anything we can do professionally all lumped together! We met running seperate businesses which have both since closed)
We will not be competing on price. We plan to be expensive but fair. Certainly not the cheapest.
What we are looking for
Business Card
I imagine a double sided business card, which will be used for more than one person. I imagine the front to be the same for everyone and the persons details to be on the back, although this is of course only my thoughts and I am of course completely open to any ideas.
The card could also have a services list or a bit about what we do on it. It might feature the website address, our business address (mail forwarding address) or our registered company number.
Or it might have none of that, we are completely open to any ideas and have no real fixed opinions. I just want it to be really nice :-)
Letterhead (secondary importance)
We will make our decision primarily on the business card, although a mathcing letterhead would be fantastic. Something standardish in format and simple, although again, all ideas are welcomed.
I hope that is enough information but if you have any questions I will answer them as fully and as quickly as possible.
Thank you once again and I really look forward to seeing your ideas and picking a winner.
Simon L.
Small businesses AND the general public
Film Production

```html
<!DOCTYPE html>
<html lang="en">
<head>
<meta charset="utf-8">
<title>Copperfield Reed – Business Cards and Letterhead</title>
<link rel="stylesheet" href="https://fonts.googleapis.com/css2?family=Arimo:ital,wght@0,400;0,700;1,400&display=swap">
<style>
  :root {
    --brand-red: #c8102e;
    --charcoal: #262b2d;
    --ink: #1d1d1b;
    --paper: #ffffff;
    --edge: #222222;
  }
  * { box-sizing: border-box; margin: 0; padding: 0; }
  html, body { width: 1200px; height: 1085px; overflow: hidden; background: var(--paper); }
  body { font-family: "Arimo", Arial, sans-serif; color: var(--ink); position: relative; }

  .sheet { position: absolute; border: 1px solid var(--edge); background: var(--paper); }
  .band { position: absolute; background: var(--charcoal); height: 11px; }
  .stripes { position: absolute; display: flex; flex-direction: column; gap: 16px; }
  .stripes span { display: block; height: 11px; background: var(--brand-red); }

  .wordmark { position: absolute; display: flex; align-items: center; gap: 6px;
    color: var(--brand-red); font-weight: 700; letter-spacing: 0.02em; white-space: nowrap; }
  .wordmark .mark { background: var(--brand-red); flex: none; }

  .reg-no { position: absolute; font-size: 7px; white-space: nowrap; }
  .person { position: absolute; left: 40px; white-space: nowrap; }
  .person .name { color: var(--brand-red); font-weight: 700; font-size: 15px; }
  .person .role { font-style: italic; font-size: 13px; }
  .details { position: absolute; left: 40px; font-size: 10px; line-height: 13px; white-space: nowrap; }
  .details .label { color: var(--brand-red); font-weight: 700; }
  .web { position: absolute; font-size: 12.5px; white-space: nowrap; }

  .services { position: absolute; left: 91px; top: 731px; list-style: none; font-size: 11px; line-height: 14px; }
  .services li { display: flex; align-items: center; gap: 3px; }
  .services li::before { content: ""; width: 15px; height: 5px; background: var(--brand-red); }

  .letter-address { position: absolute; right: 64px; top: 97px; text-align: right; font-size: 12.5px; line-height: 15px; }
  .letter-web { position: absolute; right: 63px; top: 1006px; font-size: 15px; }
  .letter-legal { position: absolute; left: 409px; width: 766px; top: 1051px; text-align: center; font-size: 9.5px; }
</style>
</head>
<body>

  <!-- Business card: Simon -->
  <section class="sheet card" style="left:22px;top:117px;width:329px;height:202px;"></section>
  <div class="stripes" style="left:350px;top:146px;width:33px;"><span></span><span></span><span></span><span></span><span></span></div>
  <div class="wordmark" style="left:40px;top:139px;font-size:13px;"><span class="mark" style="width:14px;height:14px;"></span>COPPERFIELD REED</div>
  <div class="reg-no" style="left:190px;top:163px;">Company Reg. No: 09264183</div>
  <div class="person" style="top:185px;"><span class="name">Simon Latchford</span> <span class="role">Web Developer</span></div>
  <div class="details" style="top:210px;">
    <div><span class="label">Telephone:</span> 01632 418 720</div>
    <div><span class="label">Email:</span> simon@copperfieldreed.example</div>
    <div>Copperfield Reed Ltd.</div>
    <div>212 Marlowe Row</div>
    <div>London, EC2R 8KT</div>
  </div>
  <div class="web" style="left:183px;top:278px;">www.copperfieldreed.example</div>
  <div class="band" style="left:0;top:292px;width:380px;"></div>

  <!-- Business card: Martin -->
  <section class="sheet card" style="left:22px;top:378px;width:329px;height:202px;"></section>
  <div class="stripes" style="left:331px;top:408px;width:52px;"><span></span><span></span><span></span><span></span><span></span></div>
  <div class="wordmark" style="left:40px;top:400px;font-size:13px;"><span class="mark" style="width:14px;height:14px;"></span>COPPERFIELD REED</div>
  <div class="reg-no" style="left:190px;top:424px;">Company Reg. No: 09264183</div>
  <div class="person" style="top:446px;"><span class="name">Martin Oakley</span> <span class="role">Photographer</span></div>
  <div class="details" style="top:471px;">
    <div><span class="label">Telephone:</span> 01632 418 720</div>
    <div><span class="label">Email:</span> martin@copperfieldreed.example</div>
    <div>Copperfield Reed Ltd.</div>
    <div>212 Marlowe Row</div>
    <div>London, EC2R 8KT</div>
  </div>
  <div class="web" style="left:183px;top:539px;">www.copperfieldreed.example</div>
  <div class="band" style="left:0;top:553px;width:380px;"></div>

  <!-- Business card: front -->
  <section class="sheet card" style="left:24px;top:640px;width:328px;height:202px;"></section>
  <div class="wordmark" style="left:72px;top:680px;font-size:20px;gap:8px;"><span class="mark" style="width:22px;height:22px;"></span>COPPERFIELD REED</div>
  <ul class="services">
    <li>Professional Photography</li>
    <li>Web Solutions &amp; E-Commerce</li>
    <li>Audio &amp; HD Video Production</li>
    <li>Marketing &amp; Promotions</li>
    <li>Design, Creation and Inspiration</li>
  </ul>
  <div class="band" style="left:2px;top:814px;width:380px;"></div>

  <!-- Letterhead -->
  <section class="sheet letterhead" style="left:409px;top:0;width:767px;height:1084px;"></section>
  <div class="wordmark" style="left:928px;top:48px;font-size:18px;gap:7px;"><span class="mark" style="width:20px;height:20px;"></span>COPPERFIELD REED</div>
  <address class="letter-address" style="font-style:normal;">
    <div>Copperfield Reed Ltd.</div>
    <div>212 Marlowe Row</div>
    <div>London, EC2R 8KT</div>
  </address>
  <div class="stripes" style="left:1136px;top:160px;width:51px;"><span></span><span></span><span></span><span></span><span></span></div>
  <div class="letter-web">www.copperfieldreed.example</div>
  <div class="band" style="left:375px;top:1027px;width:825px;"></div>
  <div class="letter-legal">Copperfield Reed is a Ltd Company registered in England &amp; Wales, Registration No. 09264183. Company Reg. No: 09264183</div>

</body>
</html>
```